Guarding One's Body Using Sharp Steel Cover

Hi we are producing a self defense course entitled Guarding One's Body Using Sharp Steel: A Complete Manual For Learning The Finest And Handiest Wilderness Tool In Recorded History.

I listed this as a book cover but it will actually be a DVD set, but the book cover model works fine.

See below for design examples - I am thinking we need a cover that will appeal to military/survival type people.

Target Market(s)

survivalists, cops, preppers, gun owners, martial artists, and average people wanting to learn how to defend themselves

Industry/Entity Type

Defense

Requirements
Must have
• Title: GUARDING ONE'S BODY USING SHARP STEEL: A COMPLETE MANUAL FOR LEARNING THE FINEST AND HANDIEST WILDERNESS TOOL IN RECORDED HISTORY
Nice to have
• Please look at these sample designs from other books as a model:
• https://files.plorvexa.org/media/en/4/27/BrindelQXMP.jpg - This stye is ideal.
• Other good examples:
• https://pics2.talvorn.com/8143907_k370.jpg
• http://m.zephquill.com/titles/2719058463k/48071935.jpg
• http://img.crondelmart.com/pics/P/73Tm58QyzFr._BX_KL410_TR316,410_.jpg
• http://3.cdn.wendoplix.net/-RTyZWLMMKAQ/BNWq_hufxaT/BBBBBBBBv8G/DKNp815ZaXW/s1600/Q4710392.JPG

```html
<!DOCTYPE html>
<html lang="en">
<head>
<meta charset="utf-8">
<title>Guarding One's Body Using Sharp Steel — Cover</title>
<link rel="stylesheet" href="https://fonts.googleapis.com/css2?family=Alfa+Slab+One&display=swap">
<style>
  :root {
    --page-bg: #ffffff;
    --cover-green: #7f9436;
    --cover-green-light: #98ab4a;
    --cover-green-dark: #63752a;
    --ink: #0d0d0a;
    --title-pale: #eff0a2;
    --band: #050505;
    --author-green: #7a8c33;
    --art-light: #a7b562;
    --art-dark: #56662a;
  }
  * { margin: 0; padding: 0; box-sizing: border-box; }
  html, body {
    width: 1200px;
    height: 1200px;
    overflow: hidden;
    background: var(--page-bg);
  }
  .canvas {
    width: 1200px;
    height: 1200px;
    display: flex;
    align-items: center;
    justify-content: center;
  }
  .cover {
    position: relative;
    width: 780px;
    height: 1060px;
    background:
      radial-gradient(ellipse at 30% 25%, var(--cover-green-light) 0%, transparent 55%),
      radial-gradient(ellipse at 75% 70%, var(--cover-green-dark) 0%, transparent 60%),
      var(--cover-green);
    font-family: "Alfa Slab One", Georgia, serif;
    color: var(--ink);
    text-align: center;
    overflow: hidden;
  }
  .title {
    position: absolute;
    top: 180px;
    left: 0;
    right: 0;
    line-height: 1;
    text-transform: uppercase;
  }
  .title-line { display: block; }
  .title-line + .title-line { margin-top: 6px; }
  .title-big { font-size: 66px; }
  .title-small { font-size: 38px; }
  .title-feature {
    display: block;
    margin-top: 6px;
    font-size: 178px;
    letter-spacing: 6px;
    color: var(--title-pale);
    line-height: 1;
  }
  .knife-art {
    position: absolute;
    top: 560px;
    left: 190px;
    width: 420px;
    height: 90px;
  }
  .subtitle {
    position: absolute;
    top: 680px;
    left: 60px;
    right: 60px;
    font-size: 34px;
    line-height: 1.12;
    text-transform: uppercase;
  }
  .author-band {
    position: absolute;
    left: 0;
    right: 0;
    bottom: 0;
    height: 150px;
    background: var(--band);
    display: flex;
    align-items: center;
    justify-content: center;
  }
  .author-name {
    font-size: 34px;
    color: var(--author-green);
    letter-spacing: 1px;
  }
</style>
</head>
<body>
  <main class="canvas">
    <article class="cover">
      <h1 class="title">
        <span class="title-line"><span class="title-big">Guarding</span> <span class="title-small">One's</span></span>
        <span class="title-line"><span class="title-big">Body</span> <span class="title-small">Using Sharp</span></span>
        <span class="title-feature">Steel</span>
      </h1>

      <svg class="knife-art" viewBox="0 0 420 90" role="img" aria-label="Illustration of a fixed-blade combat knife lying diagonally">
        <defs>
          <linearGradient id="knifeTone" x1="0" y1="0" x2="1" y2="0">
            <stop offset="0" stop-color="var(--art-light)"/>
            <stop offset="1" stop-color="var(--art-dark)"/>
          </linearGradient>
        </defs>
        <rect x="0" y="0" width="420" height="90" rx="45" fill="url(#knifeTone)" opacity="0.55"/>
      </svg>

      <p class="subtitle">A Complete Manual For<br>Learning The Finest<br>And Handiest Wilderness<br>Tool In Recorded<br>History</p>

      <footer class="author-band">
        <span class="author-name">AUTHORS NAME</span>
      </footer>
    </article>
  </main>
</body>
</html>
```